Online Home Automation business needs business card design

New business starting up that sells home-automation products in Australia. Business card needs to look very polished and professional. The business name is "Finch Automation".
Updates

Thank you all for the great designs, We are really impressed. We are in the process of deciding on a design but keep the designs coming in.

Industry/Entity Type

Business

```html
<!DOCTYPE html>
<html lang="en">
<head>
<meta charset="utf-8">
<title>Finch Automation – Business Card</title>
<link rel="stylesheet" href="https://fonts.googleapis.com/css2?family=Josefin+Sans:wght@300&family=PT+Sans:wght@400&display=swap">
<style>
  :root {
    --page: #ffffff;
    --card-black: #070808;
    --card-white: #ffffff;
    --accent-red: #d3202b;
    --band-grey: #3b3c3e;
    --band-grey-light: #5c5d60;
    --ring-grey: #8a8b8d;
    --text-dark: #1a1a1a;
    --text-light: #c9c9c9;
  }
  * { margin: 0; padding: 0; box-sizing: border-box; }
  html, body {
    width: 927px;
    height: 1200px;
    overflow: hidden;
    background: var(--page);
  }
  .sheet {
    position: relative;
    width: 927px;
    height: 1200px;
  }
  .card {
    position: absolute;
    left: 182px;
    width: 586px;
    height: 326px;
    background: var(--card-black);
    overflow: hidden;
  }
  .card--front {
    top: 184px;
    border: 1px solid #444;
    box-shadow: 8px 10px 10px rgba(0, 0, 0, 0.45);
  }
  .card--back {
    top: 590px;
    height: 328px;
  }
  .card__bands {
    position: absolute;
    inset: 0;
    width: 100%;
    height: 100%;
  }
  .brand {
    position: absolute;
    left: 22px;
    top: 17px;
    display: flex;
    align-items: center;
    gap: 12px;
  }
  .brand__dot {
    width: 82px;
    height: 82px;
    border-radius: 50%;
    background: var(--card-black);
  }
  .brand__name {
    font-family: "PT Sans", sans-serif;
    font-weight: 400;
    font-size: 29px;
    line-height: 1.05;
    color: var(--text-dark);
  }
  .contact {
    position: absolute;
    left: 366px;
    top: 222px;
    padding-left: 12px;
    border-left: 3px solid #6e6f72;
    font-family: "Josefin Sans", sans-serif;
    font-weight: 300;
    font-size: 12.5px;
    line-height: 16.5px;
    letter-spacing: 0.9px;
    color: var(--text-light);
    list-style: none;
  }
  .emblem {
    position: absolute;
    left: 178px;
    top: 53px;
    width: 222px;
    height: 222px;
    border-radius: 50%;
    border: 6px solid var(--ring-grey);
    display: flex;
    align-items: center;
    justify-content: center;
    text-align: center;
    font-family: "PT Sans", sans-serif;
    font-weight: 400;
    font-size: 30px;
    line-height: 1.1;
    color: var(--card-white);
  }
</style>
</head>
<body>
<main class="sheet">

  <section class="card card--front" aria-label="Business card front">
    <svg class="card__bands" viewBox="0 0 586 326" preserveAspectRatio="none" aria-hidden="true">
      <defs>
        <linearGradient id="frontBand" x1="0" y1="0" x2="1" y2="0">
          <stop offset="0" stop-color="#2a2b2d"/>
          <stop offset="0.55" stop-color="#4a4b4e"/>
          <stop offset="1" stop-color="#2f3032"/>
        </linearGradient>
      </defs>
      <rect x="0" y="0" width="586" height="106" fill="var(--card-white)"/>
      <rect x="0" y="106" width="586" height="4" fill="var(--accent-red)"/>
      <path d="M0,110 H586 V176 C420,140 220,135 0,160 Z" fill="url(#frontBand)"/>
      <path d="M0,126 C200,118 420,122 586,150 V176 C420,146 220,140 0,160 Z" fill="#1b1c1d" opacity="0.6"/>
    </svg>

    <div class="brand">
      <span class="brand__dot" aria-hidden="true"></span>
      <p class="brand__name">Finch<br>Automation</p>
    </div>

    <ul class="contact">
      <li>Address: Text text text text</li>
      <li>Tel .:+00 000 000 00 00</li>
      <li>Mob.:+00 000 000 00 00</li>
      <li>e-male: office@finchhome.net</li>
    </ul>
  </section>

  <section class="card card--back" aria-label="Business card back">
    <svg class="card__bands" viewBox="0 0 586 328" preserveAspectRatio="none" aria-hidden="true">
      <defs>
        <linearGradient id="backBand" x1="0" y1="0" x2="1" y2="0">
          <stop offset="0" stop-color="#2c2d2f"/>
          <stop offset="0.6" stop-color="#55565a"/>
          <stop offset="1" stop-color="#6a6b6e"/>
        </linearGradient>
      </defs>
      <path d="M0,0 H586 V60 C420,40 220,28 0,34 Z" fill="url(#backBand)"/>
      <path d="M0,0 H586 V36 C420,22 220,14 0,18 Z" fill="#1d1e20" opacity="0.7"/>
    </svg>

    <div class="emblem">Finch<br>Automation</div>
  </section>

</main>
</body>
</html>
```